Beautiful Quotes For Social Media Posts

We are looking for 5 beautifully designed quotes for our social media account.

Inspiration of styles we like in both style and color along with a few of our favorite fonts (you are NOT limited to these fonts this is just to give you an idea):
https://morrowstudio.example.net/s/k7p2q9x4m1t8v3n6b5c0z2w8y4j1

*These fonts are property of Morrow Studio. You do not have permission/rights to use them outside of this assignment*

Quotes to use (5):
“Only those who dare to fail greatly can ever achieve greatly.” –Walter J. Simmons
“Don’t go through life, grow through life.” – Neil Ashcombe
“Follow your bliss and the universe will open doors where there were only walls.” – Martin Oakley
“If you don’t like the road you’re walking, start paving another one.” – Greta Vance
“Life is like riding a bicycle. To keep your balance, you must keep moving.” —Oskar Feldmann

File Specifics:
- JPG
- 10x10 in size (square)
- Please include @MorrowStudio in the bottom right left or center of each design

Brand Details:
Soft but rich pastel and bright colors.
Hand Drawn florals, doodles and art
Handwritten looking fonts
Artsy, Creative, Girl and Inspiring

```html
<!DOCTYPE html>
<html lang="en">
<head>
<meta charset="utf-8">
<title>Follow your bliss – quote post</title>
<link rel="stylesheet" href="https://fonts.googleapis.com/css2?family=Chewy&family=Montserrat:wght@500&display=swap">
<style>
  :root {
    --navy: #262d3f;
    --paper: #ffffff;
    --gold: #d8a93a;
    --gold-light: #f1cf6a;
    --rose: #f2a9b3;
    --rose-deep: #de8290;
    --blush: #f7d4d6;
    --mauve: #b58a98;
    --leaf: #9fb8a4;
    --ink: #000000;
  }
  html, body {
    margin: 0;
    padding: 0;
    overflow: hidden;
    background: var(--paper);
  }
  .post {
    position: relative;
    width: 1200px;
    height: 1200px;
    overflow: hidden;
    background: repeating-linear-gradient(
      to bottom,
      var(--paper) 0 46px,
      var(--navy) 46px 93px
    );
  }
  .quote-card {
    position: absolute;
    left: 183px;
    top: 183px;
    width: 834px;
    height: 828px;
    box-sizing: border-box;
    border: 14px solid var(--gold);
    background: var(--paper);
  }
  .quote {
    position: absolute;
    left: 183px;
    top: 314px;
    width: 834px;
    margin: 0;
    text-align: center;
    font-family: "Chewy", "Arial Rounded MT Bold", "Arial Black", sans-serif;
    font-weight: 400;
    font-size: 72px;
    line-height: 105.5px;
    color: var(--ink);
    letter-spacing: 0.5px;
  }
  .handle {
    position: absolute;
    left: 183px;
    top: 900px;
    width: 834px;
    margin: 0;
    text-align: center;
    font-family: "Montserrat", Arial, sans-serif;
    font-weight: 500;
    font-size: 30px;
    line-height: 40px;
    color: var(--ink);
  }
  .floral {
    position: absolute;
    background: linear-gradient(135deg, var(--leaf) 0%, var(--blush) 28%, var(--rose) 55%, var(--rose-deep) 78%, var(--mauve) 100%);
  }
  .floral-top {
    left: 200px; top: -60px; width: 760px; height: 350px;
    border-radius: 0 0 50% 50% / 0 0 60% 60%;
  }
  .floral-bottom-left {
    left: -60px; top: 640px; width: 390px; height: 620px;
    border-radius: 40% 60% 30% 50% / 35% 45% 30% 40%;
  }
  .floral-bottom-right {
    left: 860px; top: 830px; width: 400px; height: 420px;
    border-radius: 55% 40% 30% 45% / 50% 40% 30% 40%;
  }
  .glitter-dot {
    position: absolute;
    width: 58px;
    height: 58px;
    border-radius: 50%;
    background: radial-gradient(circle, var(--gold-light), var(--gold));
  }
</style>
</head>
<body>
  <main class="post">
    <div class="quote-card"></div>

    <div class="glitter-dot" style="left:167px;top:40px" role="img" aria-label="Gold glitter dot"></div>
    <div class="glitter-dot" style="left:22px;top:262px" role="img" aria-label="Gold glitter dot"></div>
    <div class="glitter-dot" style="left:123px;top:495px" role="img" aria-label="Gold glitter dot"></div>
    <div class="glitter-dot" style="left:1058px;top:250px" role="img" aria-label="Gold glitter dot"></div>
    <div class="glitter-dot" style="left:1155px;top:470px" role="img" aria-label="Gold glitter dot"></div>
    <div class="glitter-dot" style="left:1118px;top:-5px" role="img" aria-label="Gold glitter dot"></div>
    <div class="glitter-dot" style="left:530px;top:1043px" role="img" aria-label="Gold glitter dot"></div>
    <div class="glitter-dot" style="left:1053px;top:710px" role="img" aria-label="Gold glitter dot"></div>

    <div class="floral floral-top" role="img" aria-label="Watercolour cluster of pink and mauve roses with green and plum leaves"></div>
    <div class="floral floral-bottom-left" role="img" aria-label="Watercolour pink roses with sage leaves and berry sprigs"></div>
    <div class="floral floral-bottom-right" role="img" aria-label="Watercolour pink and cream roses with plum leaves"></div>

    <p class="quote">Follow your<br>bliss and the<br>universe will open<br>doors where there<br>were only walls</p>
    <p class="handle">@MorrowStudio</p>
  </main>
</body>
</html>
```